Business card for Northland's Blue Wagon.

Good day i am looking for a business card design for my business.
The name of the business is Northland's Blue Wagon. It is a van rental business that provides a driver and helper to the customer. Customer have use to van for small moves, studio or 1 bedroom, Moving furniture like couch or kitchen cabinets.
We are available evenings, weekends and holidays.
the means to contact us is by phone at 628-947-2071; By emails at Oakridge@northlandsbluewagon.net; or by social media, Facebook and Instagram.
You can see attached pictures of the van and or logo.

```html
<!DOCTYPE html>
<html lang="en">
<head>
<meta charset="utf-8">
<title>Northland's Blue Wagon – Business Card</title>
<link rel="stylesheet" href="https://fonts.googleapis.com/css2?family=Playfair+Display:wght@400;700&display=swap">
<style>
  :root {
    --page: #d3d4d6;
    --card-white: #ffffff;
    --card-black: #181818;
    --brand-red: #c8080e;
    --ink: #222222;
    --muted: #333333;
  }
  * { margin: 0; padding: 0; box-sizing: border-box; }
  html, body {
    width: 900px; height: 1200px; overflow: hidden;
    background: var(--page);
    font-family: "Playfair Display", Georgia, serif;
  }
  .card {
    position: absolute;
    width: 630px; height: 358px;
    border-radius: 14px;
    overflow: hidden;
  }
  .card-front { left: 135px; top: 215px; background: var(--card-white); }
  .card-back { left: 136px; top: 628px; background: var(--card-black); }

  .front-mark {
    position: absolute; left: 0; right: 0; top: 0; bottom: 0;
    display: flex; align-items: center; justify-content: center;
  }
  .brand-wordmark {
    color: var(--brand-red);
    font-weight: 700;
    font-size: 34px;
    text-align: center;
    line-height: 1.15;
  }

  .back-panel { position: absolute; left: 0; top: 0; }

  .badge-circle {
    position: absolute;
    left: 328px; top: 50px;
    width: 260px; height: 260px;
    border-radius: 50%;
    background: var(--card-white);
    border: 2px solid var(--card-black);
    display: flex; align-items: center; justify-content: center;
  }
  .badge-circle .brand-wordmark { font-size: 25px; width: 190px; }

  .business-name {
    position: absolute; left: 39px; top: 38px;
    color: var(--brand-red); font-weight: 700; font-size: 30px;
    white-space: nowrap;
  }
  .person-name {
    position: absolute; left: 39px; top: 124px;
    color: var(--brand-red); font-weight: 700; font-size: 25px;
  }
  .person-title {
    position: absolute; left: 40px; top: 157px;
    color: var(--muted); font-size: 15px;
  }
  .contact-list { list-style: none; position: absolute; left: 39px; top: 188px; }
  .contact-list li {
    display: flex; align-items: center; gap: 6px;
    height: 30px;
    color: var(--ink); font-size: 15px; letter-spacing: 0.2px;
  }
  .contact-list .phone { letter-spacing: 2px; }
  .contact-list svg { width: 14px; height: 14px; fill: var(--brand-red); flex: none; }
  .social-row {
    position: absolute; left: 39px; top: 292px;
    display: flex; align-items: center; gap: 8px;
    color: var(--ink); font-size: 15px;
  }
  .social-dot { width: 19px; height: 19px; border-radius: 50%; background: var(--brand-red); }
</style>
</head>
<body>

<section class="card card-front">
  <div class="front-mark">
    <div class="brand-wordmark">Northland's Blue Wagon</div>
  </div>
</section>

<section class="card card-back">
  <svg class="back-panel" width="630" height="358" viewBox="0 0 630 358" aria-hidden="true">
    <path d="M0 20 H420 Q470 20 500 50 L500 300 Q470 338 420 338 H0 Z" fill="var(--brand-red)"/>
    <path d="M0 30 H415 Q460 30 488 58 L488 292 Q460 328 415 328 H0 Z" fill="var(--card-white)"/>
  </svg>

  <div class="badge-circle">
    <div class="brand-wordmark">Northland's Blue Wagon</div>
  </div>

  <h1 class="business-name">Northland's Blue Wagon</h1>
  <h2 class="person-name">Daniel Ostrowski</h2>
  <p class="person-title">Director</p>

  <ul class="contact-list">
    <li class="phone">
      <svg viewBox="0 0 24 24"><path d="M6.6 10.8a15.1 15.1 0 0 0 6.6 6.6l2.2-2.2a1 1 0 0 1 1-.25 11.4 11.4 0 0 0 3.6.6 1 1 0 0 1 1 1V20a1 1 0 0 1-1 1A17 17 0 0 1 3 4a1 1 0 0 1 1-1h3.5a1 1 0 0 1 1 1c0 1.25.2 2.45.6 3.6a1 1 0 0 1-.25 1z"/></svg>
      628-947-2071
    </li>
    <li>
      <svg viewBox="0 0 24 24"><path d="M2 5h20v14H2z" /><path d="M2 5l10 8 10-8" fill="none" stroke="#fff" stroke-width="1.6"/></svg>
      Oakridge@northlandsbluewagon.net
    </li>
    <li>
      <svg viewBox="0 0 24 24"><circle cx="12" cy="12" r="10"/><path d="M2 12h20M12 2v20M12 2c-4 4-4 16 0 20M12 2c4 4 4 16 0 20M4 7h16M4 17h16" fill="none" stroke="#fff" stroke-width="1.2"/></svg>
      northlandsbluewagon.net
    </li>
  </ul>

  <div class="social-row">
    <span class="social-dot"></span>
    @northlandsbluewagon
  </div>
</section>

</body>
</html>
```